wood grain ultrasonic essential oil aroma diffuser

Design a package that is simple but luxurious for the diffuser with my logo. My business is called “Gentle Ember Path”. The logo incorporates “Thoughts become things” the concept is positive thinking. I don’t particularly want the product featured as I have like to develop a uniform look for packaging and website and there are 2 different diffusers,

Target Market(s)

People interested in yoga, meditation, metaphysical aspects

Industry/Entity Type

Health And Wellness

Colors

Designer to choose colors to be used in the design.

Requirements
Must have
• Luxurious feel to packaging and alignment with the website

```html
<!DOCTYPE html>
<html lang="en">
<head>
<meta charset="utf-8">
<title>Gentle Ember Path – Ultrasonic Aroma Diffuser Package</title>
<link rel="stylesheet" href="https://fonts.googleapis.com/css2?family=Josefin+Sans:wght@400;600&display=swap">
<style>
  :root {
    --backdrop: #d9dde1;
    --box-black: #0c0c0c;
    --gold-light: #d7ad38;
    --gold-deep: #8c6512;
    --gold-line: #c9a12d;
    --ink: #1a1a1a;
    --silver: #e6e6e6;
  }
  html, body {
    margin: 0;
    padding: 0;
    width: 1200px;
    height: 848px;
    overflow: hidden;
    background: var(--backdrop);
  }
  .canvas {
    position: relative;
    width: 1200px;
    height: 848px;
  }
  .package-front {
    position: absolute;
    left: 375px;
    top: 76px;
    width: 450px;
    height: 695px;
  }
  .package-front text {
    font-family: "Josefin Sans", sans-serif;
  }
  .brand-name { font-size: 19px; font-weight: 600; fill: var(--ink); }
  .product-line { font-size: 29px; font-weight: 400; fill: var(--silver); letter-spacing: 1.5px; }
  .product-name { font-size: 46px; font-weight: 600; fill: var(--silver); letter-spacing: 11px; }
  .web-address { font-size: 11px; font-weight: 400; fill: var(--silver); letter-spacing: 3.5px; }
</style>
</head>
<body>
<main class="canvas">
  <svg class="package-front" viewBox="0 0 450 695" xmlns="http://www.w3.org/2000/svg" role="img" aria-label="Front panel of the Gentle Ember Path ultrasonic aroma diffuser box">
    <defs>
      <linearGradient id="gold-foil" x1="0" y1="0" x2="1" y2="1">
        <stop offset="0" stop-color="var(--gold-deep)"/>
        <stop offset="0.5" stop-color="var(--gold-light)"/>
        <stop offset="1" stop-color="var(--gold-deep)"/>
      </linearGradient>
    </defs>

    <rect class="box-face" x="0" y="0" width="450" height="695" fill="var(--box-black)"/>

    <path class="gold-crest" d="M23,13 H428 V90 C400,72 370,80 330,105 C270,145 200,200 130,200 C85,200 55,188 23,175 Z" fill="url(#gold-foil)"/>

    <rect class="outer-frame" x="23" y="13" width="405" height="612" fill="none" stroke="var(--gold-line)" stroke-width="3"/>

    <g class="brand-mark">
      <circle cx="133" cy="75" r="40" fill="var(--ink)"/>
      <text class="brand-name" x="45" y="152">Gentle Ember Path</text>
    </g>

    <rect class="title-frame" x="43" y="313" width="365" height="232" fill="none" stroke="var(--gold-line)" stroke-width="3"/>
    <text class="product-line" x="225" y="398" text-anchor="middle">Ultrasonic Aroma</text>
    <text class="product-name" x="230" y="465" text-anchor="middle">DIFFUSER</text>

    <text class="web-address" x="225" y="664" text-anchor="middle">www.gentleemberpath.org</text>
  </svg>
</main>
</body>
</html>
```